rk motor purge engine carbon clean

hi need leaflet done a5 size colour front and back i have all the information that needs to go on, i need background colour as carbon fiber look same as google type in veltoria green i have attached all the colours i want veltoria green and in silver attach 2 the writing i want need to look amazing also attached my logo and one picture off the car engine which maybe go on the back off the flyer my mobile number there if you need me thanks
Updates

Hi needs to be a5 flyer and front and back colour add all the writing thanks and bulet points Added Wednesday, July 22, 2015

Target Market(s)

cars,hgv plant and marine engines, fleet operators

Industry/Entity Type

Automotive

Colors
36b9a5

Requirements
Must have
• VELTORIA green colour and carbon fiber background
Nice to have
• a5 portrait bullet points both pages

```html
<!DOCTYPE html>
<html lang="en">
<head>
<meta charset="utf-8">
<title>RK Motor Purge – A5 Leaflet</title>
<link rel="stylesheet" href="https://fonts.googleapis.com/css2?family=Exo+2:wght@600;700;800&family=Open+Sans:wght@400;600&family=Orbitron:wght@700&display=swap">
<style>
  :root {
    --bg: #e9e9e9;
    --page: #0b0c0d;
    --teal: #36b9a5;
    --text: #e6e8e8;
    --shadow: rgba(0,0,0,.35);
  }
  * { box-sizing: border-box; margin: 0; padding: 0; }
  html, body { width: 867px; height: 1200px; overflow: hidden; background: var(--bg); }
  body { position: relative; font-family: "Open Sans", sans-serif; color: var(--text); }

  .page {
    position: absolute; left: 40px; width: 787px; height: 570px;
    background: var(--page); overflow: hidden; box-shadow: 0 4px 14px var(--shadow);
  }
  .page--front { top: 20px; }
  .page--back { top: 610px; }

  .photo { position: absolute; }
  .photo--car {
    left: 0; top: 0; width: 575px; height: 290px;
    background: radial-gradient(ellipse at 45% 60%, #3d4247 0%, #15181b 45%, #050607 80%);
  }
  .photo--engine-detail {
    left: 575px; top: 0; width: 212px; height: 290px;
    background: linear-gradient(120deg, #1a1c1e 0%, #5d6166 35%, #2a2d30 60%, #7b7f83 80%, #1b1d1f 100%);
  }
  .photo--engine {
    left: 20px; top: 20px; width: 330px; height: 290px;
    background: radial-gradient(ellipse at 50% 50%, #6b6f73 0%, #2d3034 50%, #0b0c0d 85%);
  }

  .brand { position: absolute; left: 20px; top: 305px; font-family: "Exo 2", sans-serif; color: var(--teal); }
  .brand__name { font-size: 40px; font-weight: 800; letter-spacing: 1px; line-height: 1; text-transform: uppercase; }
  .brand__tag { font-size: 22px; font-weight: 700; letter-spacing: 1px; margin-top: 4px; text-transform: uppercase; }

  .intro { position: absolute; left: 20px; top: 390px; width: 745px; font-size: 10.5px; line-height: 1.5; }
  .intro p + p { margin-top: 12px; }
  .intro .highlight { color: var(--teal); }

  .benefits { position: absolute; left: 430px; top: 50px; font-family: "Exo 2", sans-serif; }
  .benefits__title { color: var(--teal); font-size: 28px; font-weight: 800; line-height: 1.02; text-transform: uppercase; }
  .benefits__list { list-style: none; margin-top: 14px; }
  .benefits__list li {
    display: flex; align-items: flex-start; gap: 10px;
    font-size: 14px; font-weight: 700; line-height: 1.1; text-transform: uppercase; margin-bottom: 7px;
  }
  .tick { flex: 0 0 15px; width: 15px; height: 15px; }

  .about { position: absolute; left: 20px; top: 345px; width: 745px; font-size: 10.5px; line-height: 1.5; }

  .booking { position: absolute; left: 20px; top: 440px; }
  .booking__label { font-family: "Exo 2", sans-serif; color: var(--teal); font-size: 16px; font-weight: 800; letter-spacing: .5px; text-transform: uppercase; }
  .booking__phone { font-family: "Orbitron", sans-serif; font-size: 40px; font-weight: 700; color: #fff; letter-spacing: 2px; margin-top: 6px; }

  .contact { position: absolute; left: 430px; top: 440px; font-family: "Exo 2", sans-serif; color: var(--teal); font-size: 14px; font-weight: 700; line-height: 1.3; text-transform: uppercase; }
  .contact__social { margin-top: 10px; font-size: 11px; color: var(--text); }
  .contact__social span { display: block; color: var(--teal); font-size: 14px; }
</style>
</head>
<body>

<section class="page page--front">
  <div class="photo photo--car" role="img" aria-label="Dark sports car with glowing headlights photographed at night"></div>
  <div class="photo photo--engine-detail" role="img" aria-label="Close-up of a car engine bay with metal components"></div>

  <div class="brand">
    <div class="brand__name">RK Motor Purge</div>
    <div class="brand__tag">Carbon Clinic</div>
  </div>

  <div class="intro">
    <p>Are you on a detox so why not treat your vehicle to one? Leading a healthy lifestyle is important and this includes your vehicle too as it requires a healthy cleanse in order for it to run smooth and efficiently. The engine is the heart of travelling from A to B whether it be for business or part of your daily routine therefore it's your well-being on the road. Carbon build up is a major factor for engine complications and the latest technology now solves this problem.</p>
    <p class="highlight">An innovative approach that could save you money on fuel and garage repairs as well as maintaining a healthy engine is offered by THE CARBON CLINIC.</p>
  </div>
</section>

<section class="page page--back">
  <div class="photo photo--engine" role="img" aria-label="Chrome car engine on a dark background"></div>

  <div class="benefits">
    <h2 class="benefits__title">Benefits of<br>Motor Purge</h2>
    <ul class="benefits__list">
      <li><svg class="tick" viewBox="0 0 13 13"><rect x=".5" y=".5" width="12" height="12" fill="none" stroke="#e6e8e8"/><path d="M3 6.5l2.5 2.5L10.5 3.5" fill="none" stroke="#36b9a5" stroke-width="2"/></svg>Restores engine power</li>
      <li><svg class="tick" viewBox="0 0 13 13"><rect x=".5" y=".5" width="12" height="12" fill="none" stroke="#e6e8e8"/><path d="M3 6.5l2.5 2.5L10.5 3.5" fill="none" stroke="#36b9a5" stroke-width="2"/></svg>Lower vehicle emissions</li>
      <li><svg class="tick" viewBox="0 0 13 13"><rect x=".5" y=".5" width="12" height="12" fill="none" stroke="#e6e8e8"/><path d="M3 6.5l2.5 2.5L10.5 3.5" fill="none" stroke="#36b9a5" stroke-width="2"/></svg>Quick and hassle free</li>
      <li><svg class="tick" viewBox="0 0 13 13"><rect x=".5" y=".5" width="12" height="12" fill="none" stroke="#e6e8e8"/><path d="M3 6.5l2.5 2.5L10.5 3.5" fill="none" stroke="#36b9a5" stroke-width="2"/></svg>Smoother performance</li>
      <li><svg class="tick" viewBox="0 0 13 13"><rect x=".5" y=".5" width="12" height="12" fill="none" stroke="#e6e8e8"/><path d="M3 6.5l2.5 2.5L10.5 3.5" fill="none" stroke="#36b9a5" stroke-width="2"/></svg>Less engine vibrations</li>
      <li><svg class="tick" viewBox="0 0 13 13"><rect x=".5" y=".5" width="12" height="12" fill="none" stroke="#e6e8e8"/><path d="M3 6.5l2.5 2.5L10.5 3.5" fill="none" stroke="#36b9a5" stroke-width="2"/></svg>Green and eco-friendly</li>
      <li><svg class="tick" viewBox="0 0 13 13"><rect x=".5" y=".5" width="12" height="12" fill="none" stroke="#e6e8e8"/><path d="M3 6.5l2.5 2.5L10.5 3.5" fill="none" stroke="#36b9a5" stroke-width="2"/></svg>No dismantling of<br>engine parts</li>
    </ul>
  </div>

  <p class="about">It only takes 30 minutes to cleanse your engine back to good health depending on engine size. RK Motor Purge is a Hydrogen Therapy that cleans and revitalises your vehicle engine. When the carbon deposits are effectively removed, the engine performance is restored and revived to its former splendour. Symptoms of bad carbon buildups such as rough cold start, unpleasant engine noises and vibrations during idling or premature detonation conditions will improve significantly.</p>

  <div class="booking">
    <div class="booking__label">Call us now to make a booking</div>
    <div class="booking__phone">07700900481</div>
  </div>

  <div class="contact">
    <div>www.rkmotorpurge.com</div>
    <div>info@rkmotorpurge.com</div>
    <div class="contact__social">Find us on Facespace<span>facespace.com/rkmotorpurge</span></div>
  </div>
</section>

</body>
</html>
```